Business card - house cleaning company

We want friendly high end business card highlighting our services . NO LOGOs on back of card please.. no vertical cards NO DOUBLE BROOMS

2 owners of the company: Corinne Halvey & Joel Brandt

Included phone number: (555)318-2047

Email: brightlanetidy@mailnest.example

Website: www.brightlanetidy.example

Bonded & Insured

Alder Bend, CO 80999

Slogan maybe: Bringing a brighter shine to every corner of home

We want elegant high end card for house cleaning service. Maybe 2 sided if needed. Can it have bullet points of some services we offer

Residential Home Cleaning
Vacation Rental Cleaning
Commercial Cleaning
Carpet Cleaning
Window Cleaning
Property Management
Property Inspections
Property Maintenance
Trash Removal
Concierge Services

Highlight service on back of card. If we can do a one sided card with all this that’s great as well. Not cartoony.

Our logo attached and a design somone I had Perrin but they put very little time in. Not Unique enough. If you can do a custom design with a feminine touch that be great.

You will be eliminated for not reading the brief. NO DOUBLE LOGOS NO DOUBLE BROOMS. PLEASE BE CREATIVE. IF POST SAME LOGO WITH SMAL CHANGES RHEY WILL BE ELIMINATED. BE CREATIVE.

Thank you everyone for your designs. please only use the logo 1 time. and would love to see some that dont look all the same. We appreciate your time.

Target Market(s)

Residential and vacation rental home cleaning maid service

Industry/Entity Type

House cleaning maid services

Contact Information for Business Card

For business card use logo. black and green one provided. others for example. I wil try find some example.. We want friendly high end look. 2 owners of the company: Corinne Halvey & Joel Brandt Included phone number: (555)318-2047 Email: brightlanetidy@mailnest.example Website: www.brightlanetidy.example Bonded & Insured Estes Park, CO Slogan maybe: Bringing a brighter shine to every corner of home or Quality Service Guaranteed We want elegant high end card for house cleaning service. Maybe 2 sided if needed. Can it have bullet points of some services we offer Residential Home Cleaning Vacation Rental Cleaning Commercial Cleaning Carpet Cleaning Window Cleaning Property Management Property Inspections Property Maintenance Trash Removal Concierge Services

Requirements
Must have
• For business card use logo . Creativity. black and green one provided. We want friendly high end look. 2 owners of the company: Corinne Halvey & Joel Brandt Included phone number: (555)318-2047 Email: brightlanetidy@mailnest.example Website: www.brightlanetidy.example Licensed Bonded & Insured Estes Park, CO Slogan maybe: Bringing a brighter shine to every corner of home or Quality Service Guaranteed We want elegant high end card for house cleaning service. Maybe 2 sided if needed. Can it have bullet points of some services we offer Residential Home Cleaning Vacation Rental Cleaning Commercial Cleaning Carpet Cleaning Window Cleaning Property Management Property Inspections Property Maintenance Trash Removal Concierge Services .. creatitivty a plus. whimsical. we like stars..
Nice to have
• we want much better than the example of biz card provided as example. logo has colors that are in our website palette as well. We are open to ideas for the business card design. Will pay tip to best work. PLEASE USE COMPLIMENTING COLORS. . WE LIKE BLACK AND WHITE, stars
Should not have
• NO DOUBLE LOGOS. READ READ. READ. YOU WILL BE ELIMINATED no double logos or double brooms same side of card. I want didfrent examples. please don't make all your submission look the same

```html
<!DOCTYPE html>
<html lang="en">
<head>
<meta charset="utf-8">
<title>Brightlane Cleaning Services – Business Card</title>
<link href="https://fonts.googleapis.com/css2?family=Montserrat:wght@400;500;600;700&display=swap" rel="stylesheet">
<style>
  :root{
    --stage:#1c1c1c;
    --card-dark:#262626;
    --card-dark-2:#363636;
    --green:#6f9444;
    --green-light:#82a956;
    --blue:#2a6590;
    --white:#ffffff;
    --ink:#333333;
    --silver:#9b9b9b;
  }
  *{margin:0;padding:0;box-sizing:border-box}
  html,body{width:1200px;height:900px;overflow:hidden}
  body{background:var(--stage);font-family:"Montserrat",sans-serif;position:relative}
  .card{position:absolute;width:700px;height:400px;border-radius:18px;overflow:hidden}

  /* back side */
  .card-back{left:300px;top:35px;background:linear-gradient(135deg,var(--card-dark-2),var(--card-dark) 60%)}
  .brand-mark-back{position:absolute;right:60px;top:42px;font-size:36px;font-weight:600;color:var(--silver);letter-spacing:.5px}
  .services-title{position:absolute;left:40px;top:118px;font-size:21px;font-weight:600;color:var(--green-light);letter-spacing:2px;text-transform:uppercase}
  .service-list{position:absolute;list-style:none;color:var(--white);font-size:16px;font-weight:500;text-transform:uppercase;letter-spacing:.8px;line-height:23px}
  .service-list li{display:flex;align-items:center}
  .service-list li::before{content:"";width:11px;height:11px;border-radius:50%;background:var(--green-light);margin-right:12px;flex:none}
  .service-list.left{left:40px;top:152px}
  .service-list.right{left:380px;top:228px}
  .divider{position:absolute;left:380px;top:210px;width:290px;height:1px;background:var(--blue)}
  .slogan-band{position:absolute;left:0;bottom:0;width:100%;height:46px;background:var(--green);border-top:3px solid var(--blue);display:flex;align-items:center;padding-left:40px}
  .slogan{color:var(--white);font-size:15px;font-weight:500;text-transform:uppercase;letter-spacing:1.6px}

  /* front side */
  .card-front{left:200px;top:465px;background:var(--white)}
  .front-art{position:absolute;inset:0}
  .brand-mark-front{position:absolute;left:40px;top:44px;font-size:34px;font-weight:600;color:var(--blue);letter-spacing:.3px;line-height:1.1}
  .owners{position:absolute;right:40px;top:84px;text-align:right}
  .owners .names{font-size:25px;font-weight:700;color:var(--green);text-transform:uppercase;letter-spacing:1.5px;line-height:30px}
  .owners .role{font-size:17px;font-weight:500;color:var(--ink);letter-spacing:1.5px;margin-top:4px}
  .contact{position:absolute;left:40px;top:292px;list-style:none;color:var(--white);font-size:18px;font-weight:500;line-height:28px}
  .contact li{display:flex;align-items:center;gap:10px}
  .contact svg{width:15px;height:15px;flex:none}
  .credentials{position:absolute;right:40px;bottom:32px;text-align:right;color:var(--white);font-size:20px;font-weight:500;line-height:28px;letter-spacing:.5px}
</style>
</head>
<body>

<section class="card card-back" aria-label="Card back">
  <div class="brand-mark-back">Brightlane Cleaning Services</div>
  <h2 class="services-title">Services We Offer</h2>
  <ul class="service-list left">
    <li>Residential Home Cleaning</li>
    <li>Vacation Rental Cleaning</li>
    <li>Commercial Cleaning</li>
    <li>Carpet Cleaning</li>
    <li>Window Cleaning</li>
  </ul>
  <div class="divider"></div>
  <ul class="service-list right">
    <li>Property Management</li>
    <li>Property Inspections</li>
    <li>Property Maintenance</li>
    <li>Trash Removal</li>
    <li>Concierge Services</li>
  </ul>
  <div class="slogan-band"><p class="slogan">Bringing a brighter shine to every corner of home</p></div>
</section>

<section class="card card-front" aria-label="Card front">
  <svg class="front-art" viewBox="0 0 700 400" aria-hidden="true">
    <polygon points="0,196 700,272 700,284 0,208" fill="var(--blue)"/>
    <polygon points="0,214 700,290 700,400 0,400" fill="var(--green)"/>
  </svg>
  <svg class="front-art" viewBox="0 0 700 400">
    <rect x="120" y="190" width="270" height="80" rx="10" fill="var(--green-light)" role="img" aria-label="Mountain range illustration with sparkling stars"/>
    <rect x="500" y="205" width="200" height="85" rx="10" fill="var(--blue)" role="img" aria-label="Broom illustration sweeping along the stripe"/>
  </svg>

  <div class="brand-mark-front">Brightlane<br>Cleaning Services</div>

  <div class="owners">
    <p class="names">Corinne Halvey<br>&amp; Joel Brandt</p>
    <p class="role">OWNERS</p>
  </div>

  <ul class="contact">
    <li><svg viewBox="0 0 16 16"><path d="M4 1l3 3-2 2c1 2 3 4 5 5l2-2 3 3-2 3C7 15 1 9 1 3z" fill="var(--white)"/></svg>(555)318-2047</li>
    <li><svg viewBox="0 0 16 16"><rect x="1" y="3" width="14" height="10" fill="none" stroke="var(--white)" stroke-width="1.5"/><path d="M1 3l7 6 7-6" fill="none" stroke="var(--white)" stroke-width="1.5"/></svg>brightlanetidy@mailnest.example</li>
    <li><svg viewBox="0 0 16 16"><circle cx="8" cy="8" r="6.5" fill="none" stroke="var(--white)" stroke-width="1.3"/><ellipse cx="8" cy="8" rx="3" ry="6.5" fill="none" stroke="var(--white)" stroke-width="1.2"/><path d="M1.5 8h13" stroke="var(--white)" stroke-width="1.2"/></svg>www.brightlanetidy.example</li>
  </ul>

  <div class="credentials">Bonded &amp; Insured<br>Alder Bend, CO 80999</div>
</section>

</body>
</html>
```